Progressive/contemporary business card design for successful Startups as a Service Company

New logo launched in 2020. New website launched in 2021. Now that COVID is (mostly) behind us, I'm networking with more people and need a business card that matches the company/logo design aesthetic.

```html
<!DOCTYPE html>
<html lang="en">
<head>
<meta charset="UTF-8">
<title>Launchwise Business Card</title>
<link href="https://fonts.googleapis.com/css2?family=Montserrat:wght@400;500;600&display=swap" rel="stylesheet">
<style>
  :root {
    --backdrop: #1c1c1d;
    --card: #232324;
    --card-edge: #2c2c2d;
    --white: #ffffff;
    --silver: #cfcfcf;
    --accent: #1877d2;
    --icon: #2f86dd;
  }
  * { margin: 0; padding: 0; box-sizing: border-box; }
  html, body {
    width: 1200px; height: 900px; overflow: hidden;
    background: var(--backdrop);
    font-family: "Montserrat", sans-serif;
  }
  .stage { position: relative; width: 1200px; height: 900px; }
  .card {
    position: absolute; left: 260px; width: 680px; height: 389px;
    background: var(--card);
    border: 1px solid var(--card-edge);
  }
  .card--back { top: 40px; }
  .card--front { top: 471px; }

  .wordmark {
    display: flex; align-items: center; gap: 22px;
    font-weight: 400; text-transform: uppercase;
  }
  .wordmark__square { width: 44px; height: 44px; background: var(--accent); }
  .card--back .wordmark {
    position: absolute; left: 120px; top: 160px;
    font-size: 44px; letter-spacing: 12px; color: var(--silver);
  }
  .card--front .wordmark {
    position: absolute; left: 48px; top: 44px;
    font-size: 54px; letter-spacing: 13px; color: var(--white);
  }
  .card--front .wordmark__square { width: 54px; height: 54px; }

  .person { position: absolute; left: 100px; top: 165px; }
  .person__name {
    font-weight: 600; font-size: 20px; letter-spacing: 1px;
    color: var(--accent); text-transform: uppercase;
  }
  .person__title { font-size: 15px; color: var(--white); margin-top: 2px; }

  .divider {
    position: absolute; left: 100px; right: 80px; top: 232px;
    height: 1px; background: var(--accent);
  }

  .contacts {
    position: absolute; left: 100px; top: 250px;
    list-style: none; font-size: 16px; color: var(--white);
  }
  .contacts li { display: flex; align-items: center; gap: 10px; line-height: 26px; }
  .contacts svg { width: 12px; height: 12px; flex: none; }

  .address {
    position: absolute; right: 80px; bottom: 36px;
    text-align: right; font-size: 16px; line-height: 24px; color: var(--white);
  }
</style>
</head>
<body>
<main class="stage">
  <section class="card card--back" aria-label="Card back">
    <div class="wordmark"><span>Launchwise</span><span class="wordmark__square"></span></div>
  </section>

  <section class="card card--front" aria-label="Card front">
    <div class="wordmark"><span>Launchwise</span><span class="wordmark__square"></span></div>

    <div class="person">
      <div class="person__name">Daniel Reyes</div>
      <div class="person__title">Director</div>
    </div>

    <div class="divider"></div>

    <ul class="contacts">
      <li>
        <svg viewBox="0 0 12 12" aria-hidden="true"><path d="M3 1 L5 3.5 L4 5 Q5.5 7.5 7 8 L8.5 7 L11 9 L9.5 11 Q4 10 1 3 Z" fill="var(--icon)"/></svg>
        555-014-0275
      </li>
      <li>
        <svg viewBox="0 0 12 12" aria-hidden="true"><rect x="1" y="2.5" width="10" height="7" fill="none" stroke="var(--icon)" stroke-width="1.2"/><path d="M1 2.5 L6 6.5 L11 2.5" fill="none" stroke="var(--icon)" stroke-width="1.2"/></svg>
        hello@launchwise.co
      </li>
      <li>
        <svg viewBox="0 0 12 12" aria-hidden="true"><circle cx="6" cy="6" r="5" fill="none" stroke="var(--icon)" stroke-width="1.1"/><ellipse cx="6" cy="6" rx="2.2" ry="5" fill="none" stroke="var(--icon)" stroke-width="1"/><path d="M1 6 H11" stroke="var(--icon)" stroke-width="1"/></svg>
        www.launchwise.co
      </li>
    </ul>

    <address class="address" style="font-style: normal;">
      418 Alder Lane<br>
      Maple Ridge, WI 53920
    </address>
  </section>
</main>
</body>
</html>
```